Personal informs intake and New Zealand divorce form automated filling service

I need a website that has a professional appearance, take information from clients, automatically fill New Zealand divorce forms based on information gathered. The personal information are listed:
Applicant’s information

1 First name

2 Middle name ( if Any )

3 Last name

4 Date of birth

5 Address

6 Email

7 Gender

8 Mobile

9 Occupation

10 Ethnicity

11 Country of residence

12 Do you live in New Zealand permanently?

13 Do you and your spouse have children who are under age 16 who require additional care?

Spouse’s information

1 Spouse’s first name

2 Spouse’s middle name ( if any )

3 Spouse’s last name

4 Spouse’s date of birth

5 Spouse’s occupation

6 Spouse’s ethnicity

7 Mobil number

8 Address

Marriage details

1 Did either party change their name by deed poll following the marriage/ civil union.

2 Date of marriage

3 Place and Address where the marriage was solemnized?

4 What date did you start living together?

5 What date did you cease living together?

6 How did you agree to separate? ( verbal agreement, written agreement, court order, or other )

The forms are New Zealand one party/joint application for Order dissolving a marriage or civil union.
Once the forms are completed, it will be checked by a human before sending to the paid clients by email. The website needs to integrate multiple mainstream payment options.

The forms are uploaded, please view it and set up the questionnaire accordingly to ensure all questions in the forms are answered. Must be able to distinguish one party or joint application.

Please contact me if you are interested and need more information.

Updated an AI generated draft as a sample

Target Market(s)

Divorcées

Coding

Coded - Design and coding required

Number of Pages Required

1 page

Font styles to use
Sans Serif

Colors

Designer to choose colors to be used in the design.

Requirements
Must have
• A professional appearance, easy to initiate the information intake process
Nice to have
• Step by step guideline, easy to understand how the website works
Should not have
• Bright colors

```html
<!DOCTYPE html>
<html lang="en">
<head>
<meta charset="UTF-8">
<title>Complete New Zealand Divorce forms Online</title>
<link href="https://fonts.googleapis.com/css2?family=Inter:wght@400;500;600;700&display=swap" rel="stylesheet">
<style>
:root{
  --ink:#111418;
  --muted:#3a3f47;
  --placeholder:#5b6068;
  --brand:#0b4a8f;
  --line:#c9ccd1;
  --field-bg:#ffffff;
  --page-bg:#ffffff;
  --soft:#f2f3f5;
}
*{box-sizing:border-box;margin:0;padding:0}
html,body{width:1200px;height:3596px;overflow:hidden;background:var(--page-bg);font-family:'Inter',sans-serif;color:var(--ink)}
.page{position:relative;width:1200px;height:3596px}
.page-title{position:absolute;top:110px;left:0;width:1200px;text-align:center;font-size:38px;font-weight:700;letter-spacing:-.3px}
.page-lead{position:absolute;top:183px;left:0;width:1200px;text-align:center;font-size:17px;color:var(--muted)}
.type-label{position:absolute;left:251px;top:260px;font-size:19px;font-weight:500}
.type-select{position:absolute;left:652px;top:246px;width:297px;height:55px;background:var(--soft);border-radius:6px;font-size:15px;color:#6a6f77;padding:0 24px;display:flex;align-items:center;justify-content:space-between}
.card{position:absolute;left:234px;width:732px;background:#fff;border-radius:8px;box-shadow:0 4px 28px rgba(20,30,50,.07)}
.step-head{position:absolute;left:45px;display:flex;align-items:center;transform:translateY(-50%)}
.step-num{width:32px;height:32px;border-radius:50%;background:var(--brand);color:#fff;font-size:15px;font-weight:600;display:flex;align-items:center;justify-content:center}
.step-count{margin-left:12px;font-size:19px;color:var(--brand);font-weight:500;width:100px}
.step-slash{font-size:34px;font-weight:300;width:41px}
.step-title{font-size:33px;font-weight:400}
.label{position:absolute;font-size:18px;font-weight:500;line-height:22px}
.field{position:absolute;height:58px;border:1.5px solid var(--line);border-radius:6px;background:var(--field-bg);font-size:18px;color:var(--placeholder);display:flex;align-items:center;padding:0 15px;justify-content:space-between}
.c1{left:46px;width:309px}
.c2{left:377px;width:309px}
.full{left:46px;width:639px}
.small-select{left:518px;width:168px}
.question{position:absolute;left:45px;width:440px;font-size:18px;font-weight:500;line-height:27px;transform:translateY(-50%)}
.btn{position:absolute;left:45px;width:309px;height:58px;background:var(--brand);color:#fff;border-radius:6px;font-size:18px;font-weight:600;display:flex;align-items:center;justify-content:center}
.chev{width:11px;height:7px}
</style>
</head>
<body>
<div class="page">
  <h1 class="page-title">Complete New Zealand Divorce forms Online</h1>
  <p class="page-lead">Answer the questions below to automaticially fill your divorce application.</p>
  <div class="type-label">Application Type</div>
  <div class="type-select">One Party Application<svg class="chev" viewBox="0 0 11 7"><path d="M1 1l4.5 4.5L10 1" fill="none" stroke="#6a6f77" stroke-width="1.4"/></svg></div>

  <section class="card" style="top:324px;height:1170px">
    <div class="step-head" style="top:67px"><span class="step-num">1</span><span class="step-count">Step 1/5</span><span class="step-slash">/</span><span class="step-title">Application Type</span></div>
    <div class="label c1" style="top:123px">First Name</div><div class="label c2" style="top:123px">Middle Name</div>
    <div class="field c1" style="top:164px"></div><div class="field c2" style="top:164px"></div>
    <div class="label c1" style="top:244px">Last Name</div><div class="label c2" style="top:244px">Date of Birth</div>
    <div class="field c1" style="top:286px"></div><div class="field c2" style="top:286px">DD/MM/YYYY</div>
    <div class="label c1" style="top:374px">Address</div>
    <div class="field" style="top:414px;left:46px;width:637px"></div>
    <div class="label c1" style="top:502px">Gender</div><div class="label c2" style="top:502px">Email</div>
    <div class="field c1" style="top:542px;padding-left:9px">Male<svg class="chev" viewBox="0 0 11 7"><path d="M1 1l4.5 4.5L10 1" fill="none" stroke="#5b6068" stroke-width="1.4"/></svg></div><div class="field c2" style="top:542px"></div>
    <div class="label c1" style="top:631px">Mobile</div><div class="label c2" style="top:631px">Occupation</div>
    <div class="field c1" style="top:671px"></div><div class="field c2" style="top:671px"></div>
    <div class="label c1" style="top:759px">Ethnicity</div><div class="label c2" style="top:759px">Country of Residence</div>
    <div class="field c1" style="top:799px"></div><div class="field c2" style="top:799px"></div>
    <p class="question" style="top:915px">Do you live in New Zealand permanently?</p>
    <div class="field small-select" style="top:887px">Yes<svg class="chev" viewBox="0 0 11 7"><path d="M1 1l4.5 4.5L10 1" fill="none" stroke="#5b6068" stroke-width="1.4"/></svg></div>
    <p class="question" style="top:994px">Do you and your spouse have children who are under age 16 who require additional care?</p>
    <div class="field small-select" style="top:964px">Yes<svg class="chev" viewBox="0 0 11 7"><path d="M1 1l4.5 4.5L10 1" fill="none" stroke="#5b6068" stroke-width="1.4"/></svg></div>
    <div class="btn" style="top:1060px">Save and Continue</div>
  </section>

  <section class="card" style="top:1588px;height:778px">
    <div class="step-head" style="top:78px"><span class="step-num">2</span><span class="step-count">Step 2/5</span><span class="step-slash">/</span><span class="step-title">Spouse’s information</span></div>
    <div class="label c1" style="top:135px">Spouse’s First Name</div><div class="label" style="top:135px;left:381px">Spouse’s Middle Name</div>
    <div class="field c1" style="top:177px"></div><div class="field c2" style="top:177px"></div>
    <div class="label c1" style="top:257px">Spouse’s Last Name</div><div class="label c2" style="top:257px">Spouse’s Date of Birth</div>
    <div class="field c1" style="top:298px"></div><div class="field c2" style="top:298px">DD/MM/YYYY</div>
    <div class="label c1" style="top:391px">Spouse’s Occupation</div><div class="label c2" style="top:391px">Spouse’s Ethnicity</div>
    <div class="field c1" style="top:432px;padding-left:9px">Male<svg class="chev" viewBox="0 0 11 7"><path d="M1 1l4.5 4.5L10 1" fill="none" stroke="#5b6068" stroke-width="1.4"/></svg></div><div class="field c2" style="top:432px"></div>
    <div class="label c1" style="top:519px">Spouse’s Mobile</div><div class="label c2" style="top:519px">Spouse’s Address</div>
    <div class="field c1" style="top:561px"></div><div class="field c2" style="top:561px"></div>
    <div class="btn" style="top:646px">Save and Continue</div>
  </section>

  <section class="card" style="top:2428px;height:992px">
    <div class="step-head" style="top:79px"><span class="step-num">3</span><span class="step-count">Step 3/5</span><span class="step-slash">/</span><span class="step-title">Marriage details</span></div>
    <p class="question" style="top:177px">Did either party change their name by deed poll following the marriage/ civil union.</p>
    <div class="field small-select" style="top:148px">Yes<svg class="chev" viewBox="0 0 11 7"><path d="M1 1l4.5 4.5L10 1" fill="none" stroke="#5b6068" stroke-width="1.4"/></svg></div>
    <div class="label c1" style="top:234px">Date of marriage</div>
    <div class="field full" style="top:275px">DD/MM/YYYY</div>
    <div class="label full" style="top:361px">Place and Address where the marriage was solemnized?</div>
    <div class="field full" style="top:403px"></div>
    <div class="label full" style="top:486px">What date did you start living together?</div>
    <div class="field full" style="top:527px">DD/MM/YYYY</div>
    <div class="label full" style="top:615px">What date did you cease living together?</div>
    <div class="field full" style="top:657px">DD/MM/YYYY</div>
    <div class="label full" style="top:752px">How did you agree to separate?</div>
    <div class="field full" style="top:794px">verbal agreement<svg class="chev" viewBox="0 0 11 7"><path d="M1 1l4.5 4.5L10 1" fill="none" stroke="#5b6068" stroke-width="1.4"/></svg></div>
    <div class="btn" style="top:886px">Submit and Next</div>
  </section>
</div>
</body>
</html>
```